Electrical panel service sticker w Bucket truck & Logo

We have a rather plain sticker we put on lighting panels to remind customers who to call for service. We want to redesign them with brushed aluminum background. We want a remake of the sticker with the outline of a bucket truck. You'll need to find or draw the outling of a bucket truck maybe with the boom up slightly as we will get these stickers die cut.

We want LOGO with Ph.# and Email.
Electrical * Lighting * Sign Service

Target Market(s)

Commercial property managers

Industry/Entity Type

Property Management

Requirements
Must have
• Bucket Truck Outline

```html
<!DOCTYPE html>
<html lang="en">
<head>
<meta charset="UTF-8">
<title>Beacon Lamp Care – Panel Service Sticker</title>
<link href="https://fonts.googleapis.com/css2?family=Roboto:wght@500;900&family=Roboto+Condensed:wght@700&display=swap" rel="stylesheet">
<style>
  :root {
    --steel-dark: #8c8f93;
    --steel-mid: #b4b7ba;
    --steel-light: #eceded;
    --truck-tone: #7d8085;
    --brand-red: #f2051f;
    --ink: #0b0b0b;
    --white: #ffffff;
  }
  * { margin: 0; padding: 0; box-sizing: border-box; }
  html, body {
    width: 1200px;
    height: 1200px;
    overflow: hidden;
    background: #3a3a3a;
  }
  .sticker {
    position: relative;
    width: 1200px;
    height: 1200px;
    overflow: hidden;
    background:
      repeating-linear-gradient(180deg, rgba(255,255,255,0.10) 0 1px, rgba(0,0,0,0.06) 1px 2px, rgba(255,255,255,0) 2px 3px),
      linear-gradient(180deg, var(--steel-dark) 0%, var(--steel-mid) 22%, var(--steel-light) 50%, var(--steel-mid) 75%, var(--steel-dark) 100%);
    font-family: "Roboto", Arial, sans-serif;
  }
  .truck-outline {
    position: absolute;
    left: 274px;
    top: 26px;
    width: 650px;
    height: 426px;
    border-radius: 16px;
    background: linear-gradient(160deg, rgba(125,128,133,0.55) 0%, rgba(125,128,133,0.35) 60%, rgba(125,128,133,0.22) 100%);
  }
  .brand-name {
    position: absolute;
    left: 0;
    width: 1200px;
    text-align: center;
    color: var(--brand-red);
    font-weight: 900;
    font-size: 104px;
    text-transform: uppercase;
    line-height: 1;
    letter-spacing: 1px;
  }
  .brand-name--top { top: 500px; }
  .brand-name--bottom { top: 660px; }
  .contact-email {
    position: absolute;
    top: 808px;
    left: 0;
    width: 1200px;
    text-align: center;
    font-size: 62px;
    font-weight: 500;
    color: var(--ink);
    line-height: 1.1;
  }
  .contact-phone {
    position: absolute;
    top: 888px;
    left: 0;
    width: 1200px;
    text-align: center;
    font-size: 134px;
    font-weight: 900;
    color: var(--ink);
    letter-spacing: 2px;
    line-height: 1;
  }
  .service-band {
    position: absolute;
    left: 0;
    top: 978px;
    width: 1200px;
    height: 222px;
  }
  .service-list {
    position: absolute;
    left: 0;
    width: 1200px;
    text-align: center;
    font-family: "Roboto Condensed", "Arial Narrow", sans-serif;
    font-weight: 700;
    font-size: 56px;
    color: var(--white);
    line-height: 1;
  }
  .service-list--first { top: 1068px; }
  .service-list--second { top: 1130px; }
</style>
</head>
<body>
  <main class="sticker">
    <div class="truck-outline" role="img" aria-label="Line drawing of a bucket truck with its boom raised"></div>

    <div class="brand-name brand-name--top">Beacon Lamp</div>
    <div class="brand-name brand-name--bottom">Care</div>

    <p class="contact-email">Service@BeaconLampCare.com</p>
    <p class="contact-phone">877-555-0142</p>

    <svg class="service-band" viewBox="0 0 1200 222" preserveAspectRatio="none" aria-hidden="true">
      <path d="M0 0 Q600 144 1200 0 L1200 222 L0 222 Z" fill="var(--brand-red)"/>
    </svg>
    <p class="service-list service-list--first">• Roadways • Commercial</p>
    <p class="service-list service-list--second">• Sportslighting • Electrical &nbsp;• Signs</p>
  </main>
</body>
</html>
```